Letterhead Design Project

Need Letterhead and Envelpe design with One Single or Both Side pockets for a yong dynamic employee friendly IT services company. It should be professional and sleek and should look fresh.

Target Market(s)

IT Corporate

Industry/Entity Type

It Company

```html
<!DOCTYPE html>
<html lang="en">
<head>
<meta charset="utf-8">
<title>Velnor Technologies Letterhead Options</title>
<link rel="stylesheet" href="https://fonts.googleapis.com/css2?family=PT+Sans:wght@400;700&family=Questrial&family=Dancing+Script:wght@400&display=swap">
<style>
  :root {
    --backdrop: #ece6de;
    --paper: #ffffff;
    --brand-red: #c8242f;
    --rule-red: #d8464c;
    --body-grey: #565656;
    --title-grey: #4a4a4a;
    --label-ink: #111111;
  }
  * { margin: 0; padding: 0; box-sizing: border-box; }
  html, body { width: 1200px; height: 900px; overflow: hidden; }
  body {
    position: relative;
    background: var(--backdrop);
    font-family: "PT Sans", "Helvetica Neue", Arial, sans-serif;
    color: var(--body-grey);
  }
  .option-label {
    position: absolute;
    top: 28px;
    font-family: "Questrial", Arial, sans-serif;
    font-size: 28px;
    color: var(--label-ink);
    letter-spacing: 0.5px;
    width: 300px;
    text-align: center;
  }
  .option-label--one { left: 170px; }
  .option-label--two { left: 720px; }

  .sheet {
    position: absolute;
    top: 70px;
    width: 537px;
    height: 759px;
    background: var(--paper);
    box-shadow: 0 3px 12px rgba(0,0,0,0.18);
  }
  .sheet--one { left: 50px; }
  .sheet--two { left: 606px; }

  .brand {
    position: absolute;
    left: 36px;
    top: 68px;
    font-size: 16px;
    line-height: 20px;
    font-weight: 700;
    color: var(--title-grey);
    white-space: nowrap;
  }

  .letter {
    position: absolute;
    left: 37px;
    top: 173px;
    font-size: 10.6px;
    line-height: 13px;
    white-space: nowrap;
  }
  .letter__date, .letter__greeting { display: block; line-height: 17px; }
  .letter__para { margin-top: 13px; }
  .letter__para--lead { margin-top: 2px; }
  .letter__para--first { margin-top: 4px; }
  .letter__para span { display: block; }

  .signoff { position: absolute; left: 37px; top: 578px; }
  .signoff__signature {
    font-family: "Dancing Script", "Brush Script MT", cursive;
    font-size: 14px;
    color: var(--title-grey);
    line-height: 16px;
  }
  .signoff__title { font-size: 10.6px; font-weight: 700; color: var(--title-grey); line-height: 14px; }

  .footer-rule {
    position: absolute;
    height: 1px;
    background: var(--rule-red);
  }
  .sheet--one .footer-rule { left: 35px; width: 466px; top: 704px; }
  .sheet--two .footer-rule { left: 35px; width: 467px; top: 686px; }

  .footer-centered {
    position: absolute;
    left: 0; width: 100%;
    top: 712px;
    text-align: center;
    font-size: 10.4px;
    line-height: 12px;
  }
  .accent { color: var(--brand-red); }
  .sep { margin: 0 5px; }

  .footer-address, .footer-contact {
    position: absolute;
    top: 691px;
    font-size: 10.4px;
    line-height: 12px;
  }
  .footer-address { left: 38px; }
  .footer-contact { left: 355px; }
  .footer-address span.line, .footer-contact span.line { display: block; }
</style>
</head>
<body>

<div class="option-label option-label--one">OPTION-1</div>
<div class="option-label option-label--two">OPTION-2</div>

<section class="sheet sheet--one">
  <div class="brand">velnor technologies</div>
  <div class="letter">
    <span class="letter__date">May/09/2014</span>
    <span class="letter__greeting">Dear Alan,</span>
    <div class="letter__para letter__para--lead"><span>Lorem Ipsum is simply dummy text of the printing and typesetting industry. Lorem Ipsum has been</span></div>
    <div class="letter__para letter__para--first">
      <span>the industry's standard dummy text ever since the 1500s, when an unknown printer took a galley</span>
      <span>of type and scrambled it to make a type specimen book. It has survived not only five centuries, but</span>
      <span>also the leap into electronic typesetting, remaining essentially unchanged. It was popularised in the</span>
      <span>1960s with the release of Transfer sheets containing Lorem Ipsum passages, and more recently with</span>
      <span>desktop publishing software like Quill PageSetter including versions of Lorem Ipsum.</span>
    </div>
    <div class="letter__para">
      <span>Contrary to popular belief, Lorem Ipsum is not simply random text. It has roots in a piece of classical</span>
      <span>Latin literature from 45 BC, making it over 2000 years old. Robert Ellison, a Latin professor at</span>
      <span>Ashford College in Vermont, looked up one of the more obscure Latin words, consectetur,</span>
      <span>from a Lorem Ipsum passage, and going through the cites of the word in classical literature, discovered</span>
      <span>the undoubtable source. Lorem Ipsum comes from sections 1.10.32 and 1.10.33 of "de Finibus Bonorum</span>
      <span>et Malorum" (The Extremes of Good and Evil) by Aurelian, written in 45 BC. This book is a treatise on the</span>
      <span>theory of ethics, very popular during the Renaissance. The first line of Lorem Ipsum, "Lorem ipsum dolor</span>
      <span>sit amet..", comes from a line in section 1.10.32.</span>
    </div>
    <div class="letter__para">
      <span>The standard chunk of Lorem Ipsum used since the 1500s is reproduced below for those interested.</span>
      <span>Sections 1.10.32 and 1.10.33 from "de Finibus Bonorum et Malorum" by Aurelian are also reproduced in</span>
      <span>their exact original form, accompanied by English versions from the 1914 translation by H. Lindqvist.</span>
    </div>
    <div class="letter__para">
      <span>It is a long established fact that a reader will be distracted by the readable content of a page when</span>
      <span>looking at its layout. The point of using Lorem Ipsum is that it has a more-or-less normal distribution</span>
      <span>of letters, as opposed to using 'Content here, content here', making it look like readable English. Many</span>
      <span>desktop publishing packages and web page editors now use Lorem Ipsum as their default model text,</span>
      <span>and a search for 'lorem ipsum' will uncover many web sites still in their infancy. Various versions have</span>
      <span>evolved over the years, sometimes by accident, sometimes on purpose (injected humour and the like).</span>
    </div>
  </div>
  <div class="signoff">
    <div class="signoff__signature">Marcus Hale</div>
    <div class="signoff__title">Company Director</div>
  </div>
  <div class="footer-rule"></div>
  <div class="footer-centered">
    <div><span class="accent">A</span> : 118 W, Harbor Lane, Brookfield, CA 92410<span class="sep">|</span><span class="accent">P</span> : 555.014.2276<span class="sep">|</span><span class="accent">E</span> : info@velnortechnologies.com</div>
    <div>www.<span class="accent">velnortechnologies</span>.com</div>
  </div>
</section>

<section class="sheet sheet--two">
  <div class="brand">velnor technologies</div>
  <div class="letter">
    <span class="letter__date">May/09/2014</span>
    <span class="letter__greeting">Dear Alan,</span>
    <div class="letter__para letter__para--lead"><span>Lorem Ipsum is simply dummy text of the printing and typesetting industry. Lorem Ipsum has been</span></div>
    <div class="letter__para letter__para--first">
      <span>the industry's standard dummy text ever since the 1500s, when an unknown printer took a galley</span>
      <span>of type and scrambled it to make a type specimen book. It has survived not only five centuries, but</span>
      <span>also the leap into electronic typesetting, remaining essentially unchanged. It was popularised in the</span>
      <span>1960s with the release of Transfer sheets containing Lorem Ipsum passages, and more recently with</span>
      <span>desktop publishing software like Quill PageSetter including versions of Lorem Ipsum.</span>
    </div>
    <div class="letter__para">
      <span>Contrary to popular belief, Lorem Ipsum is not simply random text. It has roots in a piece of classical</span>
      <span>Latin literature from 45 BC, making it over 2000 years old. Robert Ellison, a Latin professor at</span>
      <span>Ashford College in Vermont, looked up one of the more obscure Latin words, consectetur,</span>
      <span>from a Lorem Ipsum passage, and going through the cites of the word in classical literature, discovered</span>
      <span>the undoubtable source. Lorem Ipsum comes from sections 1.10.32 and 1.10.33 of "de Finibus Bonorum</span>
      <span>et Malorum" (The Extremes of Good and Evil) by Aurelian, written in 45 BC. This book is a treatise on the</span>
      <span>theory of ethics, very popular during the Renaissance. The first line of Lorem Ipsum, "Lorem ipsum dolor</span>
      <span>sit amet..", comes from a line in section 1.10.32.</span>
    </div>
    <div class="letter__para">
      <span>The standard chunk of Lorem Ipsum used since the 1500s is reproduced below for those interested.</span>
      <span>Sections 1.10.32 and 1.10.33 from "de Finibus Bonorum et Malorum" by Aurelian are also reproduced in</span>
      <span>their exact original form, accompanied by English versions from the 1914 translation by H. Lindqvist.</span>
    </div>
    <div class="letter__para">
      <span>It is a long established fact that a reader will be distracted by the readable content of a page when</span>
      <span>looking at its layout. The point of using Lorem Ipsum is that it has a more-or-less normal distribution</span>
      <span>of letters, as opposed to using 'Content here, content here', making it look like readable English. Many</span>
      <span>desktop publishing packages and web page editors now use Lorem Ipsum as their default model text,</span>
      <span>and a search for 'lorem ipsum' will uncover many web sites still in their infancy. Various versions have</span>
      <span>evolved over the years, sometimes by accident, sometimes on purpose (injected humour and the like).</span>
    </div>
  </div>
  <div class="signoff">
    <div class="signoff__signature">Marcus Hale</div>
    <div class="signoff__title">Company Director</div>
  </div>
  <div class="footer-rule"></div>
  <div class="footer-address">
    <span class="line">3rd floor, No. 24, Lotus Plaza (Near City Motors)</span>
    <span class="line">Ridgeview Main Road</span>
    <span class="line">Lakeside – 560207</span>
  </div>
  <div class="footer-contact">
    <span class="line"><span class="accent">P</span> : 555.014.2276</span>
    <span class="line"><span class="accent">E</span> : info@velnortechnologies.com</span>
    <span class="line">www.<span class="accent">velnortechnologies</span>.com</span>
  </div>
</section>

</body>
</html>
```